TWR Handyman Service

File 2 Prep kitchen cabinets
File 3 Painting kitchen cabinets
File 4 Demo stairs
File 5 Completion Installing stair treads
File 6 Power washing deck
File 7 Completion of Sainting deck and railings
File 8 Completion of staining steps
Logo, owner name, email and web site on front cover
File 9 Demo living room floor
File 10 Completion of living room floor
Please see additional on attached flyer

Target Market(s)

Residential

Industry/Entity Type

Painting

Font styles to use
Serif
Sans Serif

Requirements
Must have
• Some Photos and type of work discerption
Front page Logo, web address, phone number, owners name and email address
Back Page see attached file 1
Nice to have
• Photo maybe in middle of flyer
Use the best text that you think will meet the needs
Should not have
• No pink colors

```html
<!DOCTYPE html>
<html lang="en">
<head>
<meta charset="utf-8">
<title>TWR Handyman Service – Trifold Brochure</title>
<link rel="stylesheet" href="https://fonts.googleapis.com/css2?family=Oswald:wght@500;600&family=Open+Sans:ital,wght@0,400;0,600;0,700;1,400&family=Playfair+Display:wght@500&display=swap">
<style>
:root{
  --blue:#5a5ec6;
  --blue-light:#d4d6f7;
  --navy:#24273b;
  --navy-deep:#1b1d2c;
  --paper:#f3f3f5;
  --ink:#3b3e52;
  --white:#ffffff;
  --stage:#e2e2e4;
}
*{box-sizing:border-box;margin:0;padding:0}
html,body{width:1200px;height:2400px;overflow:hidden}
body{background:var(--stage);font-family:"Open Sans",Arial,sans-serif;color:var(--ink);position:relative}
.spread{position:absolute;left:30px;width:1140px;height:1100px;display:flex;box-shadow:0 6px 24px rgba(0,0,0,.15)}
.spread--outside{top:60px}
.spread--inside{top:1240px}
.panel{position:relative;width:380px;height:1100px;overflow:hidden;background:var(--paper)}
.panel + .panel{border-left:1px solid rgba(0,0,0,.06)}
.photo{position:absolute}
.shape{position:absolute;left:0;top:0}
.web-bar{position:absolute;left:0;bottom:0;width:100%;height:70px;background:var(--navy);color:var(--white);display:flex;align-items:center;justify-content:center;font-weight:600;font-size:21px;letter-spacing:2px}
.web-bar::before{content:"";position:absolute;left:0;top:-8px;width:100%;height:8px;background:var(--blue)}
.brand{display:flex;align-items:center;gap:12px;color:var(--white);font-weight:700;font-size:20px;white-space:nowrap}
.brand-mark{width:38px;height:38px;border:3px solid var(--white);flex:none}

/* left flap */
.flap-head{position:absolute;left:34px;top:52px;width:312px}
.flap-title{font-family:"Oswald",sans-serif;font-weight:600;font-size:32px;line-height:1.2;color:var(--blue);white-space:nowrap}
.flap-rule{width:100%;height:2px;background:var(--navy);margin:8px 0 18px}
.checklist{list-style:none;padding-left:6px}
.checklist li{display:flex;align-items:center;gap:12px;font-style:italic;font-size:17px;line-height:1.3;color:var(--ink);margin-bottom:12px}
.tick{width:20px;height:20px;flex:none}

/* back panel */
.panel--back{background:var(--navy)}
.back-brand{position:absolute;top:150px;left:0;width:100%;justify-content:center}
.slogan{position:absolute;top:270px;width:100%;text-align:center;font-family:"Playfair Display",serif;font-weight:500;font-size:32px;line-height:1.45;color:var(--white);letter-spacing:3px}
.contact-tag{position:absolute;top:520px;left:60px;width:260px;height:44px;background:var(--blue);color:var(--white);font-family:"Oswald",sans-serif;font-size:22px;letter-spacing:1px;display:flex;align-items:center;justify-content:center}
.contact{position:absolute;top:590px;left:10px;width:360px;text-align:center;color:var(--white);font-size:16px;line-height:1.75}
.contact strong{font-size:19px}
.contact .owner{font-weight:600;margin-bottom:14px;display:block;line-height:1.3}
.social{position:absolute;top:905px;width:100%;display:flex;justify-content:center;gap:14px}
.social span{width:24px;height:24px;border-radius:50%;border:2px solid var(--white)}
.panel--back .web-bar{background:var(--blue)}
.panel--back .web-bar::before{background:var(--navy-deep)}

/* front cover */
.cover-brand{position:absolute;top:60px;right:34px}
.cover-text{position:absolute;top:340px;left:36px;width:320px}
.cover-head{font-family:"Oswald",sans-serif;font-weight:600;font-size:34px;line-height:1.18;color:var(--white);white-space:nowrap}
.cover-sub{margin-top:18px;width:250px;font-size:18px;line-height:1.4;color:var(--blue-light)}

/* inside */
.panel--intro{background:var(--navy)}
.intro-title{position:absolute;top:60px;left:36px;font-family:"Oswald",sans-serif;font-weight:600;font-size:36px;color:var(--white);letter-spacing:1px}
.intro-rule{position:absolute;top:116px;left:36px;width:308px;height:2px;background:rgba(255,255,255,.3)}
.intro-copy{position:absolute;top:140px;left:36px;width:310px;color:#d8d9e6;font-size:15.5px;line-height:1.6}
.intro-copy p{margin-bottom:16px}
.service{position:absolute;left:30px;width:320px}
.service-tag{display:inline-block;background:var(--blue);color:var(--white);font-weight:700;font-size:21px;padding:6px 40px 6px 16px;clip-path:polygon(0 0,100% 0,88% 100%,0 100%)}
.service-line{height:2px;background:var(--blue);margin-top:-2px}
.service-list{list-style:none;margin-top:12px}
.service-list li{font-size:15.5px;line-height:1.5;padding-left:18px;position:relative;color:var(--ink)}
.service-list li::before{content:"";position:absolute;left:2px;top:9px;width:7px;height:7px;background:var(--blue)}
</style>
</head>
<body>

<section class="spread spread--outside">

  <div class="panel panel--flap">
    <div class="photo" role="img" aria-label="Staircase with newly installed stair treads" style="left:0;top:560px;width:380px;height:470px;background:linear-gradient(200deg,#f1efec 0%,#d9d3cc 40%,#8d6b50 75%,#5b4231)"></div>
    <svg class="shape" width="380" height="1100" viewBox="0 0 380 1100" aria-hidden="true">
      <polygon points="380,520 380,760 250,1030 200,1030" fill="#5a5ec6" opacity=".9"/>
      <polygon points="0,520 150,520 0,720" fill="#f3f3f5"/>
    </svg>
    <div class="flap-head">
      <h2 class="flap-title">ONE CALL DOES IT ALL</h2>
      <div class="flap-rule"></div>
      <ul class="checklist">
        <li><svg class="tick" viewBox="0 0 20 20"><circle cx="10" cy="10" r="9" fill="none" stroke="#5a5ec6" stroke-width="2"/><path d="M5.5 10.5l3 3 6-6.5" fill="none" stroke="#5a5ec6" stroke-width="2"/></svg>15 years Experience</li>
        <li><svg class="tick" viewBox="0 0 20 20"><circle cx="10" cy="10" r="9" fill="none" stroke="#5a5ec6" stroke-width="2"/><path d="M5.5 10.5l3 3 6-6.5" fill="none" stroke="#5a5ec6" stroke-width="2"/></svg>Free Written Estimates</li>
        <li><svg class="tick" viewBox="0 0 20 20"><circle cx="10" cy="10" r="9" fill="none" stroke="#5a5ec6" stroke-width="2"/><path d="M5.5 10.5l3 3 6-6.5" fill="none" stroke="#5a5ec6" stroke-width="2"/></svg>Fully Insured</li>
        <li><svg class="tick" viewBox="0 0 20 20"><circle cx="10" cy="10" r="9" fill="none" stroke="#5a5ec6" stroke-width="2"/><path d="M5.5 10.5l3 3 6-6.5" fill="none" stroke="#5a5ec6" stroke-width="2"/></svg>Locally Owned</li>
        <li><svg class="tick" viewBox="0 0 20 20"><circle cx="10" cy="10" r="9" fill="none" stroke="#5a5ec6" stroke-width="2"/><path d="M5.5 10.5l3 3 6-6.5" fill="none" stroke="#5a5ec6" stroke-width="2"/></svg>Prompt Response</li>
      </ul>
    </div>
    <div class="photo" role="img" aria-label="Finished living room hardwood floor" style="left:34px;top:400px;width:150px;height:110px;background:linear-gradient(160deg,#8a5a33,#c89a64 60%,#e5d2b5)"></div>
    <div class="photo" role="img" aria-label="Living room floor during demolition" style="left:196px;top:400px;width:150px;height:110px;background:linear-gradient(160deg,#6e6a66,#a69a8b 60%,#d7cfc4)"></div>
    <div class="web-bar">www.twrhandyman.com</div>
  </div>

  <div class="panel panel--back">
    <div class="brand back-brand"><span class="brand-mark"></span>TWR Handyman Service</div>
    <p class="slogan">FIX IT.<br>REPAIR IT.<br>CHANGE IT.<br>BUILD IT.</p>
    <div class="contact-tag">CONTACT US</div>
    <div class="contact">
      <span class="owner"><strong>TWR Handyman Service</strong><br>Owner Dale Whitcomb</span>
      (207) 555-0148<br>
      dale@twrhandyman.com<br>
      www.twrhandyman.com<br>
      48 Birch Hollow Rd, Kennebunk, Maine 04043
    </div>
    <div class="social" aria-hidden="true"><span></span><span></span><span></span><span></span></div>
    <div class="web-bar">www.twrhandyman.com</div>
  </div>

  <div class="panel panel--cover">
    <div class="photo" role="img" aria-label="Stained wooden deck and railings on a grey house" style="left:0;top:470px;width:380px;height:560px;background:linear-gradient(180deg,#cfd3d6 0%,#9aa0a5 30%,#c27a3a 55%,#9b5a24 75%,#6f8f4a 100%)"></div>
    <svg class="shape" width="380" height="1100" viewBox="0 0 380 1100" aria-hidden="true">
      <polygon points="0,0 380,0 380,330 130,800 0,640" fill="#5a5ec6" opacity=".93"/>
      <polygon points="0,860 0,1030 90,1030" fill="#f3f3f5"/>
    </svg>
    <div class="brand cover-brand"><span class="brand-mark"></span>TWR Handyman Service</div>
    <div class="cover-text">
      <h1 class="cover-head">WE ARE THE SOLUTION<br>TO YOUR PROBLEMS!</h1>
      <p class="cover-sub">Serving Southern Maine For All Your Painting And Remodeling Needs</p>
    </div>
    <div class="web-bar">www.twrhandyman.com</div>
  </div>
</section>

<section class="spread spread--inside">

  <div class="panel panel--intro">
    <h2 class="intro-title">OUR SERVICES</h2>
    <div class="intro-rule"></div>
    <div class="intro-copy">
      <p>At TWR Handyman Service we are committed to client satisfaction and understanding that customer service is the foundation of our business.</p>
      <p>We are dedicated to providing our clients with quality workmanship performed in a prompt, professional manner.</p>
      <p>Our reliable team, second to none, will arrive neat in appearance and ready to work. Our technicians will treat each job, large or small, with the same care we would if we were repairing our own home.</p>
    </div>
    <div class="photo" role="img" aria-label="Stained staircase steps with wooden handrail" style="left:0;top:640px;width:380px;height:460px;background:linear-gradient(190deg,#efece8 0%,#cbbfb2 35%,#8c5f3d 70%,#4e3526)"></div>
    <svg class="shape" width="380" height="1100" viewBox="0 0 380 1100" aria-hidden="true">
      <polygon points="0,600 380,600 380,650 0,760" fill="#24273b"/>
      <polygon points="170,700 380,640 380,720 240,760" fill="#5a5ec6"/>
    </svg>
  </div>

  <div class="panel panel--services">
    <div class="service" style="top:50px">
      <span class="service-tag">Interior Painting</span>
      <div class="service-line"></div>
      <ul class="service-list">
        <li>Commercial &amp; Residential</li>
        <li>Kitchen Cabinets</li>
        <li>Painting</li>
        <li>Walls trim &amp; doors</li>
        <li>Ceiling repair</li>
        <li>Staining &amp; poly trim</li>
      </ul>
    </div>
    <div class="photo" role="img" aria-label="Freshly painted interior room with large windows" style="left:30px;top:305px;width:320px;height:190px;background:linear-gradient(160deg,#f2ece4,#d9c6ae 50%,#9a7452)"></div>
    <div class="service" style="top:545px">
      <span class="service-tag">Exterior Painting</span>
      <div class="service-line"></div>
      <ul class="service-list">
        <li>Commercial &amp; Residential</li>
        <li>New Painting &amp; Updates</li>
        <li>All types of Siding</li>
        <li>Power washing</li>
        <li>Painting &amp; staining of decks</li>
        <li>Fence cleaning painting &amp; sealing</li>
        <li>Furniture cleaning, painting &amp; sealing</li>
      </ul>
    </div>
    <div class="photo" role="img" aria-label="White painted deck railing outdoors" style="left:30px;top:860px;width:320px;height:190px;background:linear-gradient(180deg,#7f9a6a,#e9ebe8 55%,#b9bdb8)"></div>
  </div>

  <div class="panel panel--services">
    <div class="service" style="top:50px">
      <span class="service-tag">Carpentry</span>
      <div class="service-line"></div>
      <ul class="service-list">
        <li>Commercial &amp; Residential</li>
        <li>Kitchen remodeling</li>
        <li>Marble &amp; Granite countertops</li>
        <li>Bathroom remodeling</li>
        <li>Basement remodeling</li>
        <li>Bath accessories &amp; installation</li>
        <li>Drywall</li>
        <li>Room additions</li>
        <li>All types of siding</li>
        <li>Cabinetry</li>
        <li>Sheet rocking</li>
      </ul>
    </div>
    <div class="photo" role="img" aria-label="Kitchen with freshly painted dark cabinets" style="left:30px;top:450px;width:320px;height:200px;background:linear-gradient(160deg,#e8e4dc,#8f8a84 45%,#3c3a38)"></div>
    <div class="service" style="top:700px">
      <span class="service-tag">Maintenance</span>
      <div class="service-line"></div>
      <ul class="service-list">
        <li>Commercial &amp; Residential</li>
        <li>Hanging Curtains &amp; Blinds</li>
        <li>Shelving</li>
        <li>Lighting</li>
        <li>Picture hanging</li>
        <li>TV mounting</li>
        <li>Desk &amp; furniture assembly</li>
        <li>Fixture installation &amp; repair</li>
      </ul>
    </div>
  </div>
</section>

</body>
</html>
```